Whitcombe MD Crest Primary Care Business Card

Need a business card for a medical clinic targeting VIP patients. Should portray an upscale feeling. Simple, clean design. Logo and colors need to be incorporated into card. Clinic colors are gray/ silver, blues, white same as logo.
Clinic is a cash only VIP service clinic targeting higher income patients.
Tagline: "Where everyone is a VIP - Very Important Patient"

Target Market(s)

VIP, upscale

Industry/Entity Type

Medical

Contact Information for Business Card

Would like to use for cards with raised print or metallic highlight.

Requirements
Must have
• Incorporate logo, Use colors in logo
Nice to have
• Metallic detail
Should not have
• too much details or colors, other stock photos or designs

```html
<!DOCTYPE html>
<html lang="en">
<head>
<meta charset="utf-8">
<title>Whitcombe MD Crest Primary Care – Business Card</title>
<link rel="stylesheet" href="https://fonts.googleapis.com/css2?family=Lora:wght@400;700&display=swap">
<style>
  :root {
    --bg: #e9eaec;
    --navy: #3a4d63;
    --navy-ink: #3b4a5e;
    --silver: #a7adb5;
    --silver-dark: #8b9098;
    --white: #ffffff;
    --rule: #b9bcc1;
  }
  * { margin: 0; padding: 0; box-sizing: border-box; }
  html, body { width: 1200px; height: 780px; overflow: hidden; }
  body {
    background: var(--bg);
    font-family: "Lora", Georgia, serif;
    display: flex;
    align-items: center;
    justify-content: center;
    gap: 40px;
  }
  .card {
    width: 540px;
    height: 310px;
    position: relative;
    box-shadow: 0 8px 24px rgba(0,0,0,.18);
  }
  /* Front */
  .card-front {
    background: var(--navy);
    color: var(--white);
    display: flex;
    flex-direction: column;
    align-items: center;
    justify-content: center;
    text-align: center;
  }
  .brand { display: flex; flex-direction: column; align-items: center; }
  .brand-dot {
    width: 34px; height: 34px; border-radius: 50%;
    background: var(--silver);
    margin-bottom: 14px;
  }
  .brand-name {
    display: flex; align-items: center; gap: 10px;
    font-size: 17px; letter-spacing: 1px; text-transform: uppercase;
    color: var(--silver);
  }
  .brand-name::before, .brand-name::after {
    content: ""; width: 44px; height: 1px; background: var(--silver);
  }
  .brand-sub {
    font-size: 17px; letter-spacing: 1px; text-transform: uppercase;
    margin-top: 2px;
  }
  .card-front .brand-sub { color: var(--white); }
  .tagline {
    margin-top: 14px;
    font-size: 13px;
    letter-spacing: .5px;
    color: #e3e6ea;
  }
  /* Back */
  .card-back {
    background: var(--white);
    color: var(--silver-dark);
  }
  .person { position: absolute; left: 36px; top: 32px; }
  .person-name { font-size: 15px; font-weight: 700; text-transform: uppercase; color: var(--silver-dark); }
  .person-role { font-size: 12px; color: var(--navy-ink); }
  .divider {
    position: absolute; height: 1px; background: var(--rule);
  }
  .divider-mid { left: 70px; right: 150px; top: 150px; }
  .divider-low { left: 330px; right: 36px; top: 236px; }
  .contacts {
    position: absolute; left: 36px; top: 162px;
    list-style: none;
    font-size: 13px; line-height: 22px;
    color: var(--silver-dark);
  }
  .contacts li { display: flex; align-items: center; gap: 10px; }
  .contacts svg { width: 16px; height: 16px; flex: none; }
  .card-back .brand {
    position: absolute; right: 36px; top: 72px;
  }
  .card-back .brand-dot { width: 28px; height: 28px; background: var(--navy); margin-bottom: 10px; }
  .card-back .brand-name { font-size: 15px; color: var(--silver-dark); }
  .card-back .brand-name::before, .card-back .brand-name::after { background: var(--silver-dark); width: 30px; }
  .card-back .brand-sub { font-size: 15px; color: var(--navy-ink); font-weight: 700; }
  .address {
    position: absolute; right: 36px; bottom: 14px;
    text-align: right; font-size: 13px; line-height: 20px;
    color: var(--silver);
  }
</style>
</head>
<body>
  <section class="card card-front">
    <div class="brand">
      <span class="brand-dot"></span>
      <span class="brand-name">Whitcombe MD</span>
      <span class="brand-sub">Crest Primary Care</span>
    </div>
    <p class="tagline">Where everyone is a VIP - Very Important Patient</p>
  </section>

  <section class="card card-back">
    <div class="person">
      <p class="person-name">Daniel Hart</p>
      <p class="person-role">Founder</p>
    </div>

    <div class="divider divider-mid"></div>

    <ul class="contacts">
      <li>
        <svg viewBox="0 0 16 16" fill="none" stroke="#3b4a5e" stroke-width="1"><circle cx="8" cy="8" r="7.3"/><rect x="5.8" y="4" width="4.4" height="8" rx=".8"/></svg>
        (555) 284-6130
      </li>
      <li>
        <svg viewBox="0 0 16 16" fill="none" stroke="#3b4a5e" stroke-width="1"><circle cx="8" cy="8" r="7.3"/><rect x="4.2" y="5.3" width="7.6" height="5.4"/><path d="M4.2 5.3 8 8.5l3.8-3.2"/></svg>
        info@whitcombemd.com
      </li>
      <li>
        <svg viewBox="0 0 16 16" fill="none" stroke="#3b4a5e" stroke-width="1"><circle cx="8" cy="8" r="7.3"/><circle cx="8" cy="8" r="3.8"/><path d="M4.2 8h7.6M8 4.2v7.6"/></svg>
        www.whitcombemd.com
      </li>
    </ul>

    <div class="brand">
      <span class="brand-dot"></span>
      <span class="brand-name">Whitcombe MD</span>
      <span class="brand-sub">Crest Primary Care</span>
    </div>

    <div class="divider divider-low"></div>

    <address class="address" style="font-style:normal">
      PO BOX 418 Harbour Lane<br>6th street Ashford
    </address>
  </section>
</body>
</html>
```